complete wordpress website template for the tuckwell company

I need a wordpress themed website designed for a new social enterprise who provide healthy catering/food supply to schools. It needs to be the FULL/COMPLETE wordpress theme! I want it to be simple, sleek, easy to use and SEO friendly.

I am going to leave the brief pretty open as I would like to see your ideas.

I am attaching a company logo and would like the design to incorporate the colours but not in an overpowering way. Keep it clean and crisp.

The mission of the company is to provide healthy catering and food supply to students in Irish schools with an emphasis on promoting increased consumption of fruit and veg so please keep this in mind. I would like space for images on main page and lower pages or maybe an image roll but very open here so will welcome your ideas
I want to be able to add tabs to the top level as we introduce new services.
Tabs should include
Home
About us
Our service (split into primary & post primary schools)
Resources again this will be split as above
Links
Contact us
Homepage should include a news section and links to social media being relatively prominent
Updates

Reason: I was requested to extend to allow time for more submissions

I have updated the brief for the project

Thanks

Rob

Reason: this is the last extension of the deadline.  WIll provide feedback on all designs over coming days

Target Market(s)

should appeal to principals, teachers and parents

Industry/Entity Type

Catering

Requirements
Must have
• incorporate logo and this should fit in with overall colour scheme and feel
links for facebook twitter etc must be relatively prominent
Feel like website not a blog
News page on front page possibly all pages
reflect the healthy eating ethos of the company
Nice to have
• contact form istock photos

```html
<!DOCTYPE html>
<html lang="en">
<head>
<meta charset="utf-8">
<title>The Tuckwell Company</title>
<link href="https://fonts.googleapis.com/css2?family=Open+Sans:wght@300;400;600;700&family=Yanone+Kaffeesatz:wght@400;600&family=Arimo:wght@700&display=swap" rel="stylesheet">
<style>
:root{
  --green:#5aa51c;--green-dark:#3d860f;--green-light:#8fd13f;--lime:#d7ff5a;
  --orange:#f7931e;--orange-dark:#e0660f;--red:#e8501a;
  --blue:#1a7ac0;--blue-dark:#1b5a91;--navy:#16466f;
  --ink:#222;--grey:#e5e5e1;--line:#c9d3dc;
}
*{box-sizing:border-box;margin:0;padding:0}
html,body{width:940px;height:1200px;overflow:hidden;background:#fff}
body{position:relative;font-family:"Open Sans",sans-serif;color:var(--ink);font-size:10px}
.abs{position:absolute}
.topline{left:0;top:0;width:940px;height:4px;background:var(--green)}
.callbar{left:553px;top:0;width:368px;height:39px;background:linear-gradient(#6fbf28,var(--green));border-radius:0 0 0 14px;color:var(--lime);font-family:Arimo,sans-serif;font-weight:700;font-size:16px;line-height:37px;padding-left:16px;white-space:nowrap}
.callbar b{color:#fff}
.callbar svg{vertical-align:-4px;margin:0 3px}
.logo-disc{left:143px;top:8px;width:108px;height:108px;border-radius:50%;background:#f4f4f4;border:4px solid #e2e2e2}
.logo-name{left:34px;top:46px;width:240px;font-weight:700;font-size:21px;color:var(--blue);line-height:1}
.nav{left:239px;top:84px;width:682px;height:42px}
.nav ul{position:absolute;left:48px;top:14px;list-style:none;display:flex;font-size:12px}
.nav li{padding:0 10px;border-left:1px solid #333;line-height:12px}
.nav li:first-child{border:0;padding-left:0;color:#1a9bd9}
.search{left:728px;top:98px;width:180px;height:19px;background:#fff;border:1px solid #aaa;font-size:9px;color:#999;padding:3px 4px}
.search svg{position:absolute;right:3px;top:2px}
.hero{left:19px;top:128px;width:902px;height:305px;background:#fff;box-shadow:0 0 4px #bbb}
.hero-text{left:7px;top:7px;width:379px;height:289px;background:var(--grey)}
.hero h1{position:absolute;left:15px;top:30px;font-family:"Yanone Kaffeesatz",sans-serif;font-weight:400;font-size:24px;color:#1e3a10;letter-spacing:.3px}
.hero h1 span{color:var(--orange)}
.rule{position:absolute;height:1px;background:#999}
.hero p{position:absolute;left:16px;width:340px;font-size:9.8px;line-height:13px}
.btn-blue{position:absolute;background:linear-gradient(#3a9be0,var(--blue));border:2px solid #9ccbf0;border-radius:3px;color:#fff;font-weight:600;font-size:10.5px;line-height:18px;text-align:center}
.hero-photo{left:396px;top:13px;width:496px;height:278px;border:4px solid #f2c24c;background:linear-gradient(135deg,#d2782a,#e8c25b 35%,#c2392a 60%,#6a9a2f 85%,#d4a640)}
.follow-strip{left:26px;top:433px;width:889px;height:74px;background:linear-gradient(#f6f9fc,#d6e2ee);border:1px solid #cdd9e4;border-radius:0 0 10px 10px}
.btn-orange{position:absolute;background:linear-gradient(#ffae3b,var(--orange-dark));border-radius:4px;color:#fff;font-weight:700;text-align:center}
.soc{position:absolute;width:34px;height:34px;border-radius:6px;background:linear-gradient(#4aa6e8,#1c5d96);box-shadow:0 3px 3px #9ab}
.avatar{left:390px;top:2px;width:66px;height:66px;border-radius:50%;background:linear-gradient(#5a3a2a,#c99a80);border:3px solid #fff;box-shadow:0 0 3px #888}
.help{left:500px;top:10px;font-size:17px;color:#234;font-weight:300;line-height:20px}
.help b{color:var(--green);font-weight:700;font-size:21px}
.help-num{left:463px;top:34px;font-family:Arimo,sans-serif;font-weight:700;font-size:22px;line-height:26px;color:var(--green);letter-spacing:-1px}
.signin{left:636px;top:6px;width:246px;height:62px;background:linear-gradient(#2a72b5,var(--navy));border:2px solid #8fb6da;border-radius:6px;color:#fff}
.signin h3{position:absolute;left:7px;top:4px;font-weight:400;font-size:16px}
.field{position:absolute;height:19px;background:#fff;border:1px solid #9bb;color:#999;font-size:9px;padding:3px 5px}
.go{position:absolute;left:202px;top:30px;width:34px;height:19px;background:linear-gradient(#ffb040,var(--orange-dark));border-radius:2px;text-align:center;font-size:13px;line-height:19px}
.panel{background:linear-gradient(#fafcfe,#d3e0ec);border:1px solid var(--line);border-radius:8px}
.who{left:19px;top:519px;width:648px;height:292px}
.who h2{position:absolute;left:16px;top:18px;font-weight:300;font-size:22px;color:#222}
.dash{position:absolute;border-top:1px dashed #888}
.who p{position:absolute;left:18px;width:385px;font-size:9.6px;line-height:13px}
.who-photo{left:420px;top:49px;width:218px;height:229px;border-radius:6px;background:linear-gradient(160deg,#6f6b40,#c88a2a 40%,#d84a1e 60%,#7d8d2e 80%,#3f3a24)}
.btn-small{position:absolute;background:linear-gradient(#ffae3b,var(--orange-dark));border-radius:4px;color:#fff;font-size:9.5px;font-weight:600;line-height:19px;text-align:center}
.card{position:absolute;top:818px;width:207px}
.card .img{height:106px;border:1px solid #bbb;border-radius:6px}
.card h3{margin-top:10px;font-weight:400;font-size:20.5px;color:var(--red);padding-bottom:3px;border-bottom:1px dashed #999}
.card p{margin-top:9px;font-size:9.4px;line-height:13.5px;text-align:justify}
.card .more{display:inline-block;margin-top:9px;background:linear-gradient(#3a9be0,var(--blue));border-radius:3px;color:#fff;font-size:9.5px;line-height:18px;padding:0 10px;box-shadow:0 0 0 1px #1a5a90}
.fan{left:673px;top:518px;width:248px;height:45px;background:linear-gradient(#ffa63a,var(--orange-dark));border-radius:8px;color:#fff;font-size:23px;font-weight:300;line-height:45px;padding-left:26px}
.fan i{position:absolute;right:32px;top:5px;width:32px;height:32px;border-radius:6px;background:linear-gradient(#4aa6e8,#1c5d96)}
.subscribe{left:673px;top:568px;width:248px;height:156px;background:linear-gradient(var(--blue-dark),#2b7cc0);border:2px solid #a8c6e0;border-radius:8px}
.subscribe h3{position:absolute;left:8px;top:8px;color:#fff;font-weight:400;font-size:22px}
.subscribe .field{left:11px;width:222px;height:26px;line-height:18px}
.news{left:673px;top:730px;width:248px;height:271px}
.news h3{position:absolute;left:12px;top:10px;font-weight:400;font-size:22px}
.item{position:absolute;left:12px;width:225px}
.item b{display:block;color:var(--red);font-size:10.5px;padding-left:14px;position:relative}
.item b::before{content:"✣";position:absolute;left:0;color:var(--orange);font-size:9px}
.item u{display:block;padding-left:14px;font-size:9.6px;line-height:13px;margin-top:3px}
.readnews{position:absolute;left:10px;top:222px;width:226px;height:39px;background:linear-gradient(#3aa0e6,var(--blue));border:1px solid #9cc;border-radius:4px;color:#fff;font-size:22px;font-weight:300;line-height:37px;padding-left:13px}
.contact{left:673px;top:1007px;width:248px;height:108px;background:linear-gradient(var(--blue-dark),#2b7cc0);border:2px solid #a8c6e0;border-radius:8px;color:#fff}
.contact h3{position:absolute;left:8px;top:6px;font-weight:400;font-size:22px}
.contact p{position:absolute;left:10px;top:38px;font-size:10px;font-weight:700;line-height:13.5px}
.contact em{font-style:normal;color:#9cff3a}
.footer{left:0;top:1124px;width:940px;height:76px;background:linear-gradient(var(--green),var(--green-dark));border-top:2px solid var(--green-light);z-index:1}
.foot-tab{left:19px;top:1088px;width:367px;height:38px;z-index:2}
.foot-tab span{position:absolute;left:15px;top:20px;color:#fff;font-weight:700;font-size:16px;line-height:22px}
.foot-links{left:23px;top:1161px;color:#fff;font-size:10px;display:flex;z-index:2}
.foot-links span{padding:0 12px;border-left:1px solid #fff;line-height:10px}
.foot-links span:first-child{border:0;padding-left:0}
.copy{right:16px;top:1161px;color:#fff;font-size:10px;line-height:10px;z-index:2}
</style>
</head>
<body>
<div class="abs topline"></div>
<div class="abs callbar">Questions? Call US<svg width="18" height="18" viewBox="0 0 24 24"><path fill="#fff" d="M6.6 10.8a15 15 0 0 0 6.6 6.6l2.2-2.2c.3-.3.7-.4 1-.2 1.1.4 2.3.6 3.6.6.6 0 1 .4 1 1V20c0 .6-.4 1-1 1A17 17 0 0 1 3 4c0-.6.4-1 1-1h3.5c.6 0 1 .4 1 1 0 1.3.2 2.5.6 3.6.1.3 0 .7-.2 1z"/></svg><b>555 0142 0199</b></div>

<div class="abs logo-disc"></div>
<div class="abs logo-name">The Tuckwell Company</div>

<div class="abs nav">
  <svg class="abs" width="682" height="42" style="left:0;top:0"><path d="M0 42 C25 40 30 2 55 2 H682 V42 Z" fill="#5aa51c"/><path d="M52 9 H676 V42 H38 C48 30 45 12 52 9Z" fill="#fff"/></svg>
  <ul><li>Home</li><li>About Us</li><li>Our Services</li><li>Resources</li><li>Links</li><li>Contact Us</li></ul>
</div>
<div class="abs search">Type Your keywords here<svg width="14" height="14" viewBox="0 0 14 14"><circle cx="8" cy="6" r="4.5" fill="none" stroke="#222" stroke-width="1.6"/><path d="M5 9 1 13" stroke="#222" stroke-width="2"/></svg></div>

<section class="abs hero">
  <div class="abs hero-text">
    <h1>WELCOME TO <span>THE TUCKWELL COMPANY</span></h1>
    <div class="rule" style="left:14px;top:60px;width:352px"></div>
    <p style="top:72px">Lorem ipsum dolor sit amet, consectetur adipiscing elit. Etiam accumsan lorem sit amet lorem fermentum vitae dapibus mi viverra. Cras sagittis consectetur sollicitudin. Proin ultrices turpis at quam aliquet nec condimentum erat consequat. Cras euismod facilisis viverra. Sed diam velit, elementum eu consequat sit amet.</p>
    <p style="top:157px">Proin ultrices turpis at quam aliquet nec condimentum erat consequat. Cras euismod facilisis viverra. Sed diam velit, elementum eu consequat sit amet.</p>
    <div class="rule" style="left:14px;top:220px;width:352px"></div>
    <div class="btn-blue" style="left:13px;top:237px;width:99px">↳ read more</div>
  </div>
  <div class="abs hero-photo" role="img" aria-label="Photo of assorted fresh fruit: melons, papaya, grapes, apples and pineapple"></div>
</section>

<section class="abs follow-strip">
  <div class="btn-orange" style="left:6px;top:24px;width:140px;height:30px;font-size:15px;line-height:30px">Follow Us On</div>
  <i class="soc" style="left:160px;top:18px" aria-label="social link"></i>
  <i class="soc" style="left:204px;top:18px" aria-label="social link"></i>
  <i class="soc" style="left:248px;top:18px" aria-label="social link"></i>
  <i class="soc" style="left:291px;top:18px" aria-label="social link"></i>
  <div class="abs avatar" role="img" aria-label="Support agent photo"></div>
  <div class="abs help">need <b>HELP</b></div>
  <div class="abs help-num">555 0142 0199</div>
  <div class="abs signin">
    <h3>Sign In</h3>
    <div class="field" style="left:10px;top:30px;width:94px">Username</div>
    <div class="field" style="left:108px;top:30px;width:90px">*********</div>
    <div class="go">Go</div>
  </div>
</section>

<section class="abs panel who">
  <h2>Who we are</h2>
  <div class="dash" style="left:138px;top:41px;width:492px"></div>
  <p style="top:66px">Lorem ipsum dolor sit amet, consectetur adipiscing elit. Etiam blandit pretium odio, vitae laoreet mauris pretium nec. Suspendisse auctor egestas tincidunt. Pellentesque at neque diam, vitae condimentum felis. Pellentesque a ante mauris. Maecenas ornare massa ut nibh iaculis blandit. Integer augue magna, dapibus ac dignissim ut, molestie eget velit. Proin semper fermentum quam, quis dictum turpis vestibulum sit amet. Praesent congue pulvinar elit, sed convallis sapien egestas auctor. Cras vitae commodo diam.</p>
  <p style="top:184px">Lorem ipsum dolor sit amet, consectetur adipiscing elit. Etiam blandit pretium odio, vitae laoreet mauris pretium nec. Suspendisse auctor egestas tincidunt. Pellentesque at neque diam, vitae condimentum felis. Pellentesque a ante mauris.</p>
  <div class="btn-small" style="left:15px;top:259px;width:80px">read more »</div>
  <div class="abs who-photo" role="img" aria-label="Photo of a market stall piled with fruit and vegetables"></div>
</section>

<article class="card" style="left:21px">
  <div class="img" role="img" aria-label="Photo of a wrap with tomatoes and mozzarella" style="background:linear-gradient(135deg,#e8e4da,#c9a574 45%,#c3332a 70%,#5b8a2e)"></div>
  <h3>HYGENIC FOOD</h3>
  <p>Phasellus arcu metus, aliquam in dignissim ut, posuere eu est. Aenean elit ligula, iaculis eu tincidunt id, ultricies vitae nisl. Nunc iaculis tempus nisl. Vivamus vitae sem a risus volutpat commodo. Sed ac enim mi. Quisque</p>
  <span class="more">read more »</span>
</article>
<article class="card" style="left:239px">
  <div class="img" role="img" aria-label="Photo of carrots and root vegetables" style="background:linear-gradient(135deg,#6b8a3a,#d8c7a4 35%,#e2661c 65%,#b0481a)"></div>
  <h3>FRESH VEGETABLES</h3>
  <p>Phasellus arcu metus, aliquam in dignissim ut, posuere eu est. Aenean elit ligula, iaculis eu tincidunt id, ultricies vitae nisl. Nunc iaculis tempus nisl. Vivamus vitae sem a risus volutpat commodo. Sed ac enim mi. Quisque</p>
  <span class="more">read more »</span>
</article>
<article class="card" style="left:456px">
  <div class="img" role="img" aria-label="Photo of fruit crates at a market" style="background:linear-gradient(135deg,#8a6b3a,#c8302a 35%,#e4a23a 60%,#7aa03a)"></div>
  <h3>ALL SEASON FRUITS</h3>
  <p>Phasellus arcu metus, aliquam in dignissim ut, posuere eu est. Aenean elit ligula, iaculis eu tincidunt id, ultricies vitae nisl. Nunc iaculis tempus nisl. Vivamus vitae sem a risus volutpat commodo. Sed ac enim mi. Quisque</p>
  <span class="more">read more »</span>
</article>

<aside>
  <div class="abs fan">Become A Fan<i></i></div>
  <div class="abs subscribe">
    <h3>Subscribe Newsletter</h3>
    <div class="field" style="top:48px">Your Name</div>
    <div class="field" style="top:84px">Your email id</div>
    <div class="btn-orange" style="left:11px;top:122px;width:92px;height:27px;font-size:11px;line-height:27px;color:#222">Subscribe ⇢</div>
  </div>
  <div class="abs panel news">
    <h3>Latest News</h3>
    <div class="dash" style="left:12px;top:41px;width:225px"></div>
    <div class="item" style="top:50px"><b>Lorem Ipsum Dolor Sit Amet,</b><u>Aliquam eget sem et quam ultricies facilisis et sit amet ligula. Nam sed est vitae quam</u></div>
    <div class="item" style="top:106px"><b>Lorem Ipsum Dolor Sit Amet,</b><u>Aliquam eget sem et quam ultricies facilisis et sit amet ligula. Nam sed est vitae quam</u></div>
    <div class="item" style="top:165px"><b>Lorem Ipsum Dolor Sit Amet,</b><u>Aliquam eget sem et quam ultricies facilisis et sit amet ligula.</u></div>
    <div class="readnews">Read More News <span style="font-size:15px;margin-left:10px">»»»</span></div>
  </div>
  <div class="abs contact">
    <h3>Contact Us</h3>
    <p>12, Orchard Row,<br>Mill House, 2nd Floor,<br>Phone - <em>555 0142 0199</em><br>email - <em>info@thetuckwellcompany.com</em></p>
  </div>
</aside>

<footer class="abs footer"></footer>
<div class="abs foot-tab">
  <svg class="abs" width="367" height="38" style="left:0;top:0"><path d="M0 38 V6 Q0 0 8 0 H346 Q352 0 356 8 L367 38 Z" fill="#5aa51c"/></svg>
  <span>Follow Us On</span>
  <i class="soc" style="left:176px;top:14px" aria-label="social link"></i>
  <i class="soc" style="left:220px;top:14px" aria-label="social link"></i>
  <i class="soc" style="left:270px;top:14px" aria-label="social link"></i>
  <i class="soc" style="left:314px;top:14px" aria-label="social link"></i>
</div>
<div class="abs foot-links"><span>Home</span><span>About Us</span><span>Our Services</span><span>Resources</span><span>Links</span><span>Contact Us</span></div>
<div class="abs copy">© thetuckwellcompany.com &nbsp;|&nbsp; All Rights Reserved</div>
</body>
</html>
```